Graphic Design for a 3 Banner Tradeshow Setup

We are a Pipe Restoration company that specializes in trenchless pipelining. We need a design for a 3 banner setup to use at tradeshows. See attached "banner specs" for sizing - note the 48" x 92" will be in between the two 36" x 92" banners. See attached "Mock-Up" of information each banner needs and utilize the color scheme of the banners we already have in the "both MLD banners" AI file attached. The final designs should communicate what we do and attract people into our booth. We would like to have graphics of realistic pipes for a before (dirty pipe), after cleaning pipe, and lined pipe - see example of "pipe pictures" attached. I'm not sure if this is something you can generate or if we will need to find images of our own to send. Also, see attached "screenshot-process" to see similar images we would like to use to showcase the process.
Target Market(s)
Homeowners, Property Managers, HOA Communities, Healthcare Facilities & Hospitals, and commercial properties
Industry/Entity Type
Trenchless Pipelining
Look and feel
Each slider illustrates characteristics of the customer's brand and the style your logo design should communicate.

```html
<!DOCTYPE html>
<html lang="en">
<head>
<meta charset="utf-8">
<title>MLD Tradeshow Banners</title>
<link href="https://fonts.googleapis.com/css2?family=Russo+One&family=Michroma&family=Barlow+Condensed:wght@500;700;800&family=Barlow:wght@500&display=swap" rel="stylesheet">
<style>
:root{
  --navy:#0d1a33;
  --navy-deep:#0a1428;
  --blue:#1a4f9e;
  --blue-mid:#1f6fc2;
  --cyan:#17a6e0;
  --ice:#e6f1fb;
  --ice-2:#c8def4;
  --ink:#0b1326;
  --white:#ffffff;
  --placeholder-a:#eef2f7;
  --placeholder-b:#dde6ef;
}
*{box-sizing:border-box;margin:0;padding:0}
html,body{width:1200px;height:882px;overflow:hidden}
body{background:linear-gradient(#f2f2f2,#cfcfcf 60%,#c9c9c9);position:relative;font-family:"Barlow",sans-serif}
.banner{position:absolute;top:65px;height:736px;overflow:hidden}
.banner--side{width:288px;background:linear-gradient(var(--navy-deep) 0%,var(--navy) 30%,var(--blue) 70%,var(--blue-mid) 100%)}
.banner--left{left:73px}
.banner--right{left:837px}
.banner--center{left:408px;width:384px;background:var(--white)}

.brand{position:absolute;top:30px;left:0;width:100%;text-align:center;color:var(--white)}
.brand__name{display:flex;align-items:center;justify-content:center;gap:8px;font-family:"Russo One",sans-serif;font-size:48px;line-height:1;letter-spacing:3px}
.brand__mark{width:28px;height:28px;background:var(--blue-mid)}
.brand__tag{margin-top:4px;font-family:"Michroma",sans-serif;font-size:8.6px;letter-spacing:2.6px}

.panel{position:absolute;left:29px;top:112px;width:231px;height:480px;border-radius:14px;background:linear-gradient(160deg,var(--white),var(--ice) 45%,var(--ice-2));border:2px solid var(--cyan)}
.panel__tab{position:absolute;left:50%;top:-8px;transform:translateX(-50%);width:160px;height:28px;background:linear-gradient(var(--blue-mid),var(--blue));border-radius:0 0 14px 14px;color:var(--white);font-family:"Russo One",sans-serif;font-size:16px;letter-spacing:.5px;text-align:center;line-height:28px}

.icon{width:58px;height:58px;flex:none;border-radius:5px;background:linear-gradient(var(--blue-mid),var(--navy));border:1px solid var(--cyan);display:flex;align-items:center;justify-content:center}
.icon svg{width:40px;height:40px;fill:none;stroke:var(--white);stroke-width:2;stroke-linecap:round;stroke-linejoin:round}

.assess-item{position:absolute;left:0;width:100%;display:flex;flex-direction:column;align-items:center}
.assess-item__label{margin-top:5px;font-family:"Russo One",sans-serif;font-size:15.5px;line-height:16px;letter-spacing:1px;color:var(--ink);text-align:center}

.fix-item{position:absolute;left:17px;display:flex;align-items:center;gap:11px}
.fix-item__label{font-family:"Russo One",sans-serif;font-size:17px;line-height:18px;letter-spacing:1px;color:var(--ink)}

.photo{position:absolute;left:0;bottom:0;width:100%;height:143px}
.photo--monitors{background:linear-gradient(135deg,#2b4f8c,#1a2a4a 50%,#3a5f9a)}
.photo--reel{background:linear-gradient(135deg,#3b5a3a,#2c3a30 50%,#4c8a4c)}

.headline{position:absolute;top:18px;width:100%;text-align:center;font-family:"Russo One",sans-serif;background:linear-gradient(var(--blue),var(--cyan));-webkit-background-clip:text;background-clip:text;color:transparent}
.headline__big{font-size:86px;line-height:64px;letter-spacing:1px}
.headline__small{font-size:40px;line-height:40px;margin-top:8px;letter-spacing:1px}
.promise{position:absolute;top:133px;left:0;width:100%;height:106px;background:linear-gradient(var(--cyan),var(--blue));color:var(--white);text-align:center;font-family:"Barlow Condensed",sans-serif;font-weight:800}
.promise__lead{margin-top:13px;font-size:18px;letter-spacing:1.4px}
.promise__main{font-size:31px;line-height:27px;margin-top:4px;letter-spacing:1.6px}

.process{position:absolute;top:252px;left:20px;width:350px;height:370px;background:linear-gradient(160deg,var(--placeholder-a),var(--placeholder-b))}
.step{position:absolute;width:27px;height:27px;border-radius:50%;background:linear-gradient(var(--blue-mid),var(--navy));border:2px solid var(--white);color:var(--white);font-family:"Russo One",sans-serif;font-size:16px;text-align:center;line-height:23px}
.caption{position:absolute;font-size:9.6px;line-height:10.6px;color:var(--ink)}

.cta{position:absolute;left:17px;top:637px;width:350px;height:99px;background:linear-gradient(var(--ink),#000 55%,#2a2a2a);border-radius:10px 10px 0 0;text-align:center}
.cta__tab{position:absolute;left:39px;top:626px;width:304px;height:26px;background:var(--cyan);color:var(--white);font-family:"Barlow Condensed",sans-serif;font-weight:700;font-size:16.5px;letter-spacing:.3px;line-height:26px;text-align:center}
.cta__url{margin-top:27px;font-family:"Russo One",sans-serif;font-size:18px;color:var(--cyan);letter-spacing:2px}
.cta__phone{margin-top:4px;font-family:"Russo One",sans-serif;font-size:30px;color:var(--white);letter-spacing:2px}
</style>
</head>
<body>

<section class="banner banner--side banner--left">
  <div class="brand">
    <div class="brand__name"><span class="brand__mark"></span>MLD</div>
    <div class="brand__tag">MODERN LINE DRAINAGE</div>
  </div>
  <div class="panel">
    <div class="panel__tab">WE ASSESS</div>
    <div class="assess-item" style="top:34px">
      <div class="icon"><svg viewBox="0 0 40 40"><rect x="6" y="10" width="12" height="12" rx="2"/><path d="M12 22v10M24 8h8v24h-8zM28 8v-3"/></svg></div>
      <div class="assess-item__label">CCTV PIPE<br>INVESTIGATION</div>
    </div>
    <div class="assess-item" style="top:142px">
      <div class="icon"><svg viewBox="0 0 40 40"><path d="M4 14l8-4 8 5 8-5 8 4v10l-8 6-8-6-8 6-8-6z"/></svg></div>
      <div class="assess-item__label">SCOPE<br>DEVELOPMENT</div>
    </div>
    <div class="assess-item" style="top:250px">
      <div class="icon"><svg viewBox="0 0 40 40"><rect x="8" y="5" width="20" height="30" rx="2"/><path d="M11 10h14M12 17h3M18 17h3M12 23h3M18 23h3M12 29h3"/><circle cx="30" cy="26" r="6"/></svg></div>
      <div class="assess-item__label">BUDGETARY<br>EVALUATION</div>
    </div>
    <div class="assess-item" style="top:362px">
      <div class="icon"><svg viewBox="0 0 40 40"><circle cx="22" cy="18" r="10"/><path d="M22 8v10h10M14 26l-8 8"/></svg></div>
      <div class="assess-item__label">PROJECT<br>OVERSIGHT</div>
    </div>
  </div>
  <div class="photo photo--monitors" role="img" aria-label="Technician reviewing pipe camera footage on several monitors"></div>
</section>

<section class="banner banner--center">
  <h1 class="headline"><div class="headline__big">PIPE</div><div class="headline__small">PROBLEMS?</div></h1>
  <div class="promise">
    <div class="promise__lead">WE HELP FIX PIPE PROBLEMS</div>
    <div class="promise__main">WITHOUT HAVING TO<br>TEAR UP YOUR BUIDLING</div>
  </div>
  <div class="process" role="img" aria-label="Process illustration of a pipe being inspected, cleaned, lined and cured, with a before and after pipe cross-section"></div>
  <div class="step" style="left:212px;top:253px">1</div>
  <p class="caption" style="left:257px;top:255px">A sewer camera is used<br>to investigate the pipe to<br>determine condition</p>
  <div class="step" style="left:104px;top:330px">2</div>
  <p class="caption" style="left:40px;top:326px">The Pipe is<br>mechanically<br>cleaned</p>
  <div class="step" style="left:96px;top:446px">3</div>
  <p class="caption" style="left:19px;top:452px">A CIPP Liner is<br>pulled into place<br>and the bladder<br>inflated.</p>
  <div class="step" style="left:160px;top:550px">4</div>
  <p class="caption" style="left:89px;top:587px">After curing the bladder is<br>removed leaving behind a<br>structrial pipe within a pipe</p>
  <div class="cta">
    <div class="cta__url">WWW.MLDLINING.COM</div>
    <div class="cta__phone">1-800-555-0147</div>
  </div>
  <div class="cta__tab">CALL TODAY FOR ALL YOUR PIPE RESTORATION</div>
</section>

<section class="banner banner--side banner--right">
  <div class="brand">
    <div class="brand__name"><span class="brand__mark"></span>MLD</div>
    <div class="brand__tag">MODERN LINE DRAINAGE</div>
  </div>
  <div class="panel">
    <div class="panel__tab">WE FIX</div>
    <div class="fix-item" style="top:32px">
      <div class="icon"><svg viewBox="0 0 40 40"><path d="M8 6v16a8 8 0 0016 0v-4h10M14 6v16a2 2 0 004 0v-10h16"/></svg></div>
      <div class="fix-item__label">SLOW<br>DRAINS</div>
    </div>
    <div class="fix-item" style="top:107px">
      <div class="icon"><svg viewBox="0 0 40 40"><path d="M8 6v20M14 6v20M14 12h8a8 8 0 018 8v6M4 30c4-3 8 3 12 0s8 3 12 0 6 2 8 0M4 35h32"/></svg></div>
      <div class="fix-item__label">WATER<br>BACK - UPS</div>
    </div>
    <div class="fix-item" style="top:181px">
      <div class="icon"><svg viewBox="0 0 40 40"><path d="M12 4c-3 3 3 5 0 8s3 5 0 8M20 4c-3 3 3 5 0 8s3 5 0 8M28 4c-3 3 3 5 0 8s3 5 0 8"/><ellipse cx="20" cy="28" rx="14" ry="5"/></svg></div>
      <div class="fix-item__label">SEWER<br>ODORS</div>
    </div>
    <div class="fix-item" style="top:256px">
      <div class="icon"><svg viewBox="0 0 40 40"><path d="M4 12v12M36 12v12M4 16h32M4 20h32M18 16l2 4 2-4M20 26c-2 3-2 5 0 5s2-2 0-5"/></svg></div>
      <div class="fix-item__label">CRACKED<br>PIPES</div>
    </div>
    <div class="fix-item" style="top:330px">
      <div class="icon"><svg viewBox="0 0 40 40"><path d="M4 22v12M36 22v12M4 24h32M4 32h32M20 24v-12M20 16c-4 0-6-3-6-6 4 0 6 3 6 6M20 14c4 0 6-3 6-6-4 0-6 3-6 6M16 30l4-6 4 6"/></svg></div>
      <div class="fix-item__label">ROOT<br>INTRUSION</div>
    </div>
    <div class="fix-item" style="top:400px">
      <div class="icon"><svg viewBox="0 0 40 40"><path d="M6 8h20v8M6 12h16v6M30 6v14M8 24v10M14 24v10M18 30l14-6 2 3-14 6z"/></svg></div>
      <div class="fix-item__label">RECURRING<br>PLUMBING<br>PROBLEMS</div>
    </div>
  </div>
  <div class="photo photo--reel" role="img" aria-label="Technician in a company shirt operating a green hose reel outdoors"></div>
</section>

</body>
</html>
```